GUARANTEED WordPress design needed for a sassy, confident charisma coach!

We need a website design for Mira Haskett's brand new, responsive, Wordpress website.
Mira is a trainer / coach who teaches people how to be more charismatic and runs events, publishes video courses and has an ongoing video blog. Her old website is here: www.mirahaskett-example.co.uk ... but it's now time to have a much better site!
We have a strong idea about the technical components of the website, but we need a designer's eye to create a great style for the site (and provide layered PSD files which our developers will then convert to HTML and CSS).
Mira's brand is sassy, brave, warm and confident. The videos on her existing site give quite a good feel for her personality. We need a clean, stylish and compelling page that isn't too corporate and captures her personality. Every element needs to feel coherent, from fonts and headings to colours and spacing.
The following sites are not exactly what Mira wants (and certainly aren't right in terms of colours) but they give you an idea of the kind of people she is competing against and the area she is operating in:
http://www.fenna-troske.example/
http://brynwellow.example/
Ideally, you will have done something similar and be able to key in on exactly the kind of thing we want: we're not looking to reinvent the wheel. Hopefully you won't mind tweaking a few things if you are close to what we need.
More detail is provided in the word document attached. But in a nutshell we need: a banner, footer, sign-up strap, menu bar, signature and 4 different basic page types. We want bursts of bright colours, contrasted with black and white if possible - sorry we can't be more specific than that...
The word doc also contains some amateur mock-ups as well (the images are also just mockups at this stage) - but although these give a general sense of the structure what we are looking for, we are clearly not designers...so please help! We need a designer's touch!
Kind regards,
Tomas
PS The layered PSD versions of the mockup files are available on Quellbox: https://files.quellbox.example/sh/k27rpw4m1xqzv/QWxnEr8tLpVu3YcMd0aHs?dl=0
Project Deadline Extended Reason: We are looking for a polished, "designed" look. The mock-up that we have provided is just indicative of the features we want. Added Saturday, May 14, 2016
Entrepreneurs who need to sell themselves.
4 page

```html
<!DOCTYPE html>
<html lang="en">
<head>
<meta charset="utf-8">
<title>Mira Haskett – Charisma Coach</title>
<link href="https://fonts.googleapis.com/css2?family=Open+Sans:wght@400;600;700;800&family=Kalam:wght@700&family=Oswald:wght@500&display=swap" rel="stylesheet">
<style>
:root{
  --pink:#e63d62;
  --red:#e8503e;
  --blue:#25b4e2;
  --orange:#f4a01f;
  --green:#8dc540;
  --purple:#6a4c9c;
  --ink:#2b2b2b;
  --grey:#777;
  --line:#e2e2e2;
  --light:#f3f3f3;
  --footer:#3a3a3a;
}
*{box-sizing:border-box;margin:0;padding:0}
html,body{width:1200px;height:3584px;overflow:hidden;background:#fff}
body{position:relative;font-family:"Open Sans",Arial,sans-serif;color:var(--ink)}
.abs{position:absolute}

/* header */
.site-header{left:0;top:0;width:1200px;height:52px;background:#fff}
.brand{left:40px;top:10px;font-family:"Open Sans",Arial,sans-serif;font-weight:700;font-size:26px;color:var(--ink);display:flex;align-items:center;gap:10px}
.brand-dot{width:12px;height:12px;border-radius:50%;background:var(--pink)}
.main-nav{right:40px;top:18px;display:flex;gap:28px;font-size:13px;font-weight:600;letter-spacing:.5px}

/* hero */
.hero{left:0;top:52px;width:1200px;height:548px;background:linear-gradient(180deg,#f7f7f7,#e9e9e9)}
.pillar{display:flex;align-items:center}
.pillar-circle{border-radius:50%}
.pillar-word{font-family:"Kalam",cursive;font-size:54px;color:#5a5a5a;white-space:nowrap}
.pillar-word b{color:#fff;font-size:72px}
.hero-photo{left:700px;top:20px;width:280px;height:528px;background:linear-gradient(180deg,#d9d3cf 0%,#c93a45 45%,#b8323b 100%);border-radius:120px 120px 0 0}

/* strap */
.strap{left:80px;top:640px;width:1040px;height:280px}
.strap-photo{left:96px;top:680px;width:240px;height:240px;border-radius:50%;background:#cfcfcf;border:14px solid #8a8a8a}
.strap-photo i{position:absolute;inset:14px;border-radius:50%;background:linear-gradient(160deg,#e8e2dd,#c33b47)}
.strap-text{left:480px;top:690px;width:560px;font-size:22px;line-height:1.35;color:#0f3d52}
.field{height:44px;background:#fff;border-radius:4px;font-size:15px;color:#999;padding:11px 14px}
.yes{border-radius:50%;background:var(--purple);color:#fff;font-weight:800;font-size:15px;text-align:center;display:flex;align-items:center;justify-content:center;line-height:1.1;border:3px solid #fff;box-shadow:0 0 0 3px var(--purple)}
.strap-note{left:480px;top:876px;font-size:12px;color:#0f3d52}

/* posts */
.post-title{font-family:"Kalam",cursive;font-size:28px;line-height:40px;color:var(--ink);width:700px;left:80px;text-align:center;white-space:nowrap}
.byline{left:80px;width:700px;text-align:center;font-size:12px;color:var(--grey)}
.post-visual{left:80px;width:700px;height:340px;overflow:hidden}
.post-visual .shot{position:absolute;right:0;bottom:0;width:260px;height:300px}
.vis-text{position:absolute;font-weight:800;text-transform:uppercase;line-height:1.1;white-space:nowrap}
.excerpt{left:80px;width:700px;font-size:14px;line-height:1.65;color:var(--grey)}
.keep{left:80px;width:170px;height:36px;border:2px solid var(--red);border-radius:18px;color:var(--red);font-size:12px;font-weight:700;display:flex;align-items:center;justify-content:space-between;padding:0 4px 0 16px}
.keep span{width:26px;height:26px;border-radius:50%;background:var(--red);color:#fff;display:flex;align-items:center;justify-content:center;font-size:14px}
.rule{left:80px;width:700px;height:1px;background:var(--line)}

.pager{left:300px;top:3076px;display:flex;gap:10px;font-size:13px}
.pager span{width:30px;height:30px;border-radius:50%;border:1px solid #ccc;display:flex;align-items:center;justify-content:center;color:var(--grey)}
.pager .on{background:var(--red);border-color:var(--red);color:#fff}

/* sidebar */
.side-head{left:820px;width:300px;display:flex;align-items:center;gap:12px;font-family:"Oswald",sans-serif;font-size:24px;color:var(--pink)}
.side-head::before,.side-head::after{content:"";flex:1;height:2px;background:var(--pink)}
.tab{left:820px;top:1090px;width:300px;text-align:center;font-size:13px;font-weight:700;color:var(--pink);border-bottom:2px solid var(--pink);padding-bottom:8px}
.pop{left:820px;width:300px;font-size:13px;line-height:1.4;border-bottom:1px solid var(--line);padding-bottom:10px}
.pop em{display:block;font-style:normal;font-size:10px;font-weight:700;color:var(--pink);margin-top:3px}
.tags{left:820px;top:1608px;width:300px;text-align:center;line-height:1.5;font-weight:700;color:var(--ink)}
.event{left:820px;top:2110px;width:300px;height:460px;background:linear-gradient(180deg,#6b6b6b,#3c3c3c)}
.event-text{position:absolute;left:20px;color:#fff;font-weight:800;text-transform:uppercase}
.learn{position:absolute;left:80px;top:370px;width:120px;height:60px;background:var(--blue);color:#fff;font-weight:800;font-size:16px;text-align:center;line-height:1.2;padding-top:8px}
.story{left:820px;top:2710px;width:300px;height:250px;border:1px solid var(--line);padding:18px;font-size:13px;line-height:1.5;color:var(--grey);font-style:italic}
.avatar{position:absolute;left:110px;top:140px;width:40px;height:40px;border-radius:50%;background:#c9b8aa}
.dots{position:absolute;left:0;right:0;bottom:12px;text-align:center;letter-spacing:4px;color:#ccc;font-style:normal}

/* footer */
.site-footer{left:0;top:3160px;width:1200px;height:360px;background:var(--footer);color:#fff}
.foot-head{font-family:"Kalam",cursive;font-size:26px;color:#fff}
.video{left:80px;top:3230px;width:300px;height:170px;background:linear-gradient(135deg,#d7d2cd,#8c8c8c)}
.contact{left:420px;top:3230px;font-size:14px;line-height:1.6;color:#ddd}
.news{left:780px;top:3168px;width:340px;height:344px;background:#fff;color:var(--ink);padding:20px 24px;font-size:14px;line-height:1.45;text-align:center}
.news .field{border:1px solid #ccc;margin-top:10px;text-align:left;width:200px}
.news-note{margin-top:46px;font-size:13px;font-style:italic}
.bottom{left:0;top:3520px;width:1200px;height:64px;font-size:11px;color:var(--grey);display:flex;align-items:center;gap:34px;padding-left:80px}
.socials{right:80px;top:3536px;display:flex;gap:8px}
.socials i{width:30px;height:30px;border-radius:4px;background:var(--blue)}
</style>
</head>
<body>

<header class="abs site-header">
  <div class="abs brand">Mira Haskett <span class="brand-dot"></span></div>
  <nav class="abs main-nav"><span>EVENTS</span><span>WORK WITH ME</span><span>CORPORATE</span><span>ABOUT</span><span>CONTACT</span></nav>
</header>

<section class="abs hero">
  <div class="abs pillar" style="left:150px;top:170px">
    <div class="pillar-circle" style="width:140px;height:140px;background:var(--orange)"></div>
    <div class="pillar-word abs" style="left:30px;top:24px"><b>A</b>ttract</div>
  </div>
  <div class="abs pillar" style="left:430px;top:240px">
    <div class="pillar-circle" style="width:140px;height:140px;background:var(--blue)"></div>
    <div class="pillar-word abs" style="left:30px;top:24px"><b>C</b>onnect</div>
  </div>
  <div class="abs pillar" style="left:210px;top:350px">
    <div class="pillar-circle" style="width:140px;height:140px;background:var(--green)"></div>
    <div class="pillar-word abs" style="left:44px;top:24px"><b>I</b>nfluence</div>
  </div>
  <div class="abs hero-photo" role="img" aria-label="Photo of the coach in a red dress, hands on hips"></div>
</section>

<svg class="abs strap" viewBox="0 0 1040 280" aria-hidden="true">
  <path d="M30 0H1010a30 30 0 0 0 30 30V250a30 30 0 0 0-30 30H30a30 30 0 0 0-30-30V30A30 30 0 0 0 30 0Z" fill="var(--blue)"/>
  <path d="M40 14H1000a26 26 0 0 0 26 26V240a26 26 0 0 0-26 26H40a26 26 0 0 0-26-26V40A26 26 0 0 0 40 14Z" fill="none" stroke="#fff" stroke-width="3"/>
</svg>
<div class="abs strap-photo" role="img" aria-label="Portrait of the coach in glasses"><i></i></div>
<p class="abs strap-text">Learn how to unlock the superpower* of your charisma and win all the business you want with this FREE training.</p>
<div class="abs field" style="left:480px;top:790px;width:240px">First name</div>
<div class="abs field" style="left:740px;top:790px;width:240px">Email address</div>
<div class="abs yes" style="left:1004px;top:770px;width:88px;height:88px">YES<br>PLEASE!</div>
<p class="abs strap-note">* Promise to only use your powers for good.</p>

<!-- post 1 -->
<h2 class="abs post-title" style="top:1030px">Public speaking...made easy</h2>
<p class="abs byline" style="top:1076px">Written by Mira Haskett</p>
<div class="abs post-visual" style="top:1110px;background:var(--red)">
  <div class="vis-text" style="left:30px;top:28px;font-size:44px;color:#fff">Public speaking...</div>
  <div class="vis-text" style="left:120px;top:150px;font-size:50px;color:#2b2b2b">Made<br>easy :-)</div>
  <div class="shot" role="img" aria-label="Photo of the coach speaking into a microphone" style="width:230px;height:240px;background:linear-gradient(180deg,#e27b6e,#b8362c)"></div>
</div>
<p class="abs excerpt" style="top:1470px">Lorem ipsum dolor sit amet, consectetur adipiscing elit. Praesent fringilla tortor et mi convallis, ut scelerisque dui rhoncus. Donec quis lorem malesuada, molestie metus id, vehicula lacus. Pellentesque ultrices venenatis ullamcorper. Sed metus ligula, pharetra id risus eu, fermentum auctor eros.</p>
<div class="abs keep" style="top:1600px">KEEP READING <span>›</span></div>
<div class="abs rule" style="top:1680px"></div>

<!-- post 2 -->
<h2 class="abs post-title" style="top:1710px">Take charge of your style...Boost your confidence</h2>
<p class="abs byline" style="top:1756px">Written by Mira Haskett</p>
<div class="abs post-visual" style="top:1790px;background:var(--blue)">
  <div class="vis-text" style="left:30px;top:26px;font-size:44px;color:#fff">Take charge of your<br><span style="font-size:70px">style...</span></div>
  <div class="vis-text" style="left:30px;top:210px;font-size:44px;color:#fff">...boost your<br><span style="font-size:58px">confidence</span></div>
  <div class="shot" role="img" aria-label="Photo of the coach beside a clothing rail" style="width:220px;height:180px;top:110px;bottom:auto;background:linear-gradient(180deg,#f1d9d9,#c6434f)"></div>
</div>
<p class="abs excerpt" style="top:2150px">Lorem ipsum dolor sit amet, consectetur adipiscing elit. Praesent fringilla tortor et mi convallis, ut scelerisque dui rhoncus. Donec quis lorem malesuada, molestie metus id, vehicula lacus. Pellentesque ultrices venenatis ullamcorper. Sed metus ligula, pharetra id risus eu, fermentum auctor eros.</p>
<div class="abs keep" style="top:2280px">KEEP READING <span>›</span></div>
<div class="abs rule" style="top:2360px"></div>

<!-- post 3 -->
<h2 class="abs post-title" style="top:2390px">Unfulfilled? It's time to think about your values...</h2>
<p class="abs byline" style="top:2436px">Written by Mira Haskett</p>
<div class="abs post-visual" style="top:2470px;background:var(--orange)">
  <div class="vis-text" style="left:30px;top:30px;font-size:46px;color:#fff">Unfulfilled? It's<br>time to think<br>about your<br>values...</div>
  <div class="abs" style="left:30px;top:264px;padding:8px 20px;background:#111;color:#fff;font-weight:800;font-size:34px;white-space:nowrap">DO THIS EXERCISE NOW</div>
  <div class="shot" role="img" aria-label="Photo of the coach thinking" style="width:200px;height:250px;top:0;bottom:auto;background:linear-gradient(180deg,#e8c6a0,#8a5b3c)"></div>
</div>
<p class="abs excerpt" style="top:2830px">Lorem ipsum dolor sit amet, consectetur adipiscing elit. Praesent fringilla tortor et mi convallis, ut scelerisque dui rhoncus. Donec quis lorem malesuada, molestie metus id, vehicula lacus. Pellentesque ultrices venenatis ullamcorper. Sed metus ligula, pharetra id risus eu, fermentum auctor eros.</p>
<div class="abs keep" style="top:2960px">KEEP READING <span>›</span></div>
<div class="abs rule" style="top:3040px"></div>

<div class="abs pager"><span class="on">1</span><span>2</span><span>3</span><span>…</span><span>15</span><span>›</span></div>

<!-- sidebar -->
<h3 class="abs side-head" style="top:1030px">MIRA SAYS...</h3>
<div class="abs tab">POPULAR</div>
<div class="abs pop" style="top:1130px">Be more brave: 5 lessons we could learn from our best friends<em>TARGETS</em></div>
<div class="abs pop" style="top:1210px">Are you letting your core beliefs hold you back?<em>MINDSET</em></div>
<div class="abs pop" style="top:1290px">How I learned to stop worrying and start networking<em>NETWORKING</em></div>
<div class="abs pop" style="top:1370px">Bitchy resting face and other strange – but true – problems<em>EXPRESSION</em></div>

<h3 class="abs side-head" style="top:1550px">TAGS</h3>
<div class="abs tags">
  <span style="font-size:13px">body language</span><br>
  <span style="font-size:24px">capsule wardrobe</span><br>
  <span style="font-size:12px">confidence handshake mindset nlp passion</span> <span style="font-size:20px">power pose</span><br>
  <span style="font-size:12px">presentations presence</span><br>
  <span style="font-size:28px">rapport</span> <span style="font-size:13px">spring wear style</span><br>
  <span style="font-size:12px">values vision board warmth</span>
</div>

<h3 class="abs side-head" style="top:2050px">COMING UP</h3>
<div class="abs event" role="img" aria-label="Event poster photo of the coach on stage">
  <div class="event-text" style="top:20px;font-size:28px;line-height:1.1">Unlock the<br>superpower<br>of charisma</div>
  <div class="event-text" style="top:190px;font-size:64px">Live</div>
  <div class="event-text" style="top:280px;font-size:16px;text-transform:none;font-style:italic">* Only 6<br>places left.</div>
  <div class="learn">LEARN<br>MORE</div>
</div>

<h3 class="abs side-head" style="top:2650px">SUCCESS STORIES</h3>
<div class="abs story">
  “I’ve never been a fearless speaker, and my best ideas got lost in nerves. Two sessions later I pitched to the whole board – and they listened. Still smiling.”
  <div class="avatar" role="img" aria-label="Client portrait"></div>
  <div class="abs" style="left:160px;top:144px;font-style:normal;font-size:12px;color:var(--ink)"><b>Petra</b><br>HR Director</div>
  <div class="abs" style="left:18px;top:196px;font-size:11px;font-style:normal;color:var(--pink)">To read the full story click here</div>
  <div class="dots">● ● ● ●</div>
</div>

<!-- footer -->
<footer class="abs site-footer">
  <div class="abs foot-head" style="left:80px;top:24px">WATCH MY VIDEOS</div>
  <div class="abs foot-head" style="left:420px;top:24px">CONTACT US</div>
</footer>
<div class="abs video" role="img" aria-label="Video still of the coach with a guest"></div>
<div class="abs contact">Kennington, SE11<br><br>Tel<br>07700 900412<br><br>Email<br>mira@mirahaskett-example.co.uk</div>
<div class="abs news">
  Hey! Don't go without signing up because you'll miss out on our exclusive offers, awesome tips, and weekly motivation in my fab newsletter *.
  <div class="field">First name</div>
  <div class="field">Email address</div>
  <div class="abs yes" style="left:240px;top:170px;width:74px;height:74px;font-size:12px">YES<br>PLEASE!</div>
  <p class="news-note">* And that'll make me smile :-)</p>
</div>

<div class="abs bottom"><span>© 2016 Mira Haskett Ltd</span><span>PRIVACY POLICY</span><span>TERMS POLICY</span><span>DISCLAIMERS</span></div>
<div class="abs socials" aria-label="Social links"><i></i><i></i><i></i><i></i><i style="background:var(--red)"></i><i style="background:var(--red)"></i></div>

</body>
</html>
```